Letterhead Design Project

Initially, we would like to review our letterheads.

Something simple which uses our corporate imagery well and is nicely balanced.

Please note that I will be following up this letter-head with some customised quote templates and similarly customisable collateral in the next few weeks.

Target Market(s)

Enterprise business

Industry/Entity Type

Quote

Requirements
Must have
• The Nexora9 logo
See www.nexora9.com.au

Our tagline "Enterprise Hosting, Messaging and Server Virtualisation"

Our website address

Ideally in our colour pallette, but will consider submissions which look fantastic and necessitate other colours.

```html
<!DOCTYPE html>
<html lang="en">
<head>
<meta charset="utf-8">
<title>Nexora9 Letterhead</title>
<link rel="stylesheet" href="https://fonts.googleapis.com/css2?family=Arimo:wght@400;700&display=swap">
<style>
  :root {
    --header-top: #4d4d4d;
    --header-bottom: #000000;
    --brand-red: #e3161b;
    --paper: #ffffff;
    --tagline: #e2e2e2;
    --address: #222222;
    --url-muted: #9a9a9a;
    --url-strong: #ffffff;
  }
  * { margin: 0; padding: 0; box-sizing: border-box; }
  html, body {
    width: 928px;
    height: 1200px;
    overflow: hidden;
    background: var(--paper);
  }
  .letterhead {
    position: relative;
    width: 928px;
    height: 1200px;
    background: var(--paper);
    font-family: "Arimo", Arial, sans-serif;
  }
  .masthead {
    position: absolute;
    left: 0; top: 0;
    width: 928px;
    height: 170px;
    background: linear-gradient(to bottom, var(--header-top) 0%, #1c1c1c 55%, var(--header-bottom) 100%);
  }
  .brand {
    position: absolute;
    left: 31px;
    top: 90px;
    display: flex;
    align-items: center;
    gap: 8px;
  }
  .brand-square {
    width: 62px;
    height: 62px;
    background: var(--brand-red);
  }
  .brand-name {
    font-weight: 700;
    font-size: 72px;
    line-height: 1;
    letter-spacing: -4px;
    color: var(--url-strong);
  }
  .tagline {
    position: absolute;
    right: 17px;
    top: 138px;
    font-size: 17px;
    color: var(--tagline);
    white-space: nowrap;
  }
  .address {
    position: absolute;
    right: 735px;
    top: 1090px;
    text-align: right;
    font-size: 14.5px;
    line-height: 17.6px;
    color: var(--address);
    font-style: normal;
  }
  .footer-band {
    position: absolute;
    left: 232px;
    top: 1148px;
    width: 696px;
    height: 52px;
    background: linear-gradient(to bottom, #000000 0%, #1a1a1a 50%, #444444 100%);
  }
  .web-address {
    position: absolute;
    right: 34px;
    top: 15px;
    font-size: 18px;
    color: var(--url-muted);
  }
  .web-address strong {
    color: var(--url-strong);
    font-weight: 700;
  }
</style>
</head>
<body>
  <main class="letterhead">
    <header class="masthead">
      <div class="brand">
        <div class="brand-square"></div>
        <span class="brand-name">Nexora9</span>
      </div>
      <p class="tagline">Enterprise Hosting • Messaging • Server Virtualisation</p>
    </header>

    <address class="address">
      Nexora9 Pty. Ltd.<br>
      Suite 1, Level 2<br>
      18 Harlow Parade,<br>
      Kellbrook, Australia<br>
      VIC - 3812
    </address>

    <footer class="footer-band">
      <p class="web-address">www.<strong>nexora9</strong>.com.au</p>
    </footer>
  </main>
</body>
</html>
```